Agency Website & Personal brand

My name is Kostas Vranelis & I've been a digital marketer & an e-commerce expert since 2010.

- I've spoken to 20 different events around the world up to 3,000 people in size.
- I've sold over 1500 training courses around e-commerce growth.
- I have over 100 testimonials (video & photo) from successful students who bought my training
- I have dozens of video testimonials from respected entrepreneurs that vouch for me and my work
- I have photos with marketing legends with that I shared the stage like Owen Tarrick, Martin Fellowbrand, Glen Maro & more
- I am the host of the Aegean Roundtable since 2017 - a high-level networking event for 7 & 8 figure entrepreneurs - 100 people have come to Greece since 2017
- I have tons of videos created where I showcase my expertise on growth
- I have worked with dozens of e-commerce stores on their growth & helped them scale to multiple 6, 7 & 8 figures either on consulting

I need a website design that showcases my authority & be a lead generating machine.

The goal is to bring people on a call with me but also grab their email and start building the relationship with them and free valuable content

We have 3 offers :

1. Paid ads (Done for You)
2. Consulting/Mastermind (Done with You)
3. Training (Do it Yourself)

```html
<!DOCTYPE html>
<html lang="en">
<head>
<meta charset="utf-8">
<title>Kostas Vranelis — Digital Marketing & E-commerce Expert</title>
<link href="https://fonts.googleapis.com/css2?family=Lato:wght@400;700&family=Roboto:wght@400;500&display=swap" rel="stylesheet">
<style>
:root{
  --backdrop:#0b2a66;
  --backdrop-deep:#06204f;
  --navy:#021a45;
  --ink:#1d2230;
  --muted:#555a66;
  --soft:#9a9ea8;
  --blue:#1f6bd6;
  --sky:#4f8fe8;
  --black:#03070f;
  --white:#ffffff;
}
*{margin:0;padding:0;box-sizing:border-box}
html,body{width:1200px;height:2408px;overflow:hidden}
body{background:var(--backdrop);font-family:'Lato',sans-serif;color:var(--ink);position:relative}
.backdrop-shape{position:absolute;border-radius:50%;background:var(--backdrop-deep)}
.page{position:absolute;left:95px;top:110px;width:998px;height:2186px;background:var(--white);border-radius:16px;overflow:hidden}
.abs{position:absolute}
.btn{position:absolute;display:flex;align-items:center;justify-content:center;font-size:10px;font-weight:700;border-radius:20px;white-space:nowrap}
.btn-navy{background:var(--navy);color:var(--white)}
.btn-outline-navy{border:1.5px solid var(--navy);color:var(--navy);background:var(--white)}
.btn-blue{background:var(--blue);color:var(--white)}
.btn-outline-blue{border:1.5px solid var(--blue);color:var(--blue);background:var(--white)}

/* hero */
.hero-media{left:0;top:0;width:466px;height:566px;background:linear-gradient(135deg,#c9c4b8 0%,#8a7a5c 40%,#4a3a22 75%,#2a1f12 100%)}
.play{left:428px;top:248px;width:64px;height:64px;border-radius:50%;background:var(--white);box-shadow:0 4px 14px rgba(0,0,0,.25)}
.nav{top:54px;font-size:11px;color:var(--ink)}
.nav-cta{left:862px;top:44px;width:80px;height:31px;background:var(--navy);color:var(--white);font-size:10px;font-weight:700;display:flex;align-items:center;justify-content:center}
.hero-name{left:536px;top:128px;font-size:16px;color:var(--navy)}
.hero-title{left:536px;top:152px;font-size:45px;line-height:46px;font-weight:700;color:#2b2e36;letter-spacing:-.3px}
.hero-lead{left:536px;top:314px;width:370px;font-size:12.5px;line-height:21px;color:#3a3e48}
.stat{top:488px}
.stat b{display:block;font-size:16px;font-weight:700;color:var(--ink)}
.stat span{display:block;font-size:9.5px;color:var(--muted);margin-top:3px}

/* about */
.about{left:0;top:566px;width:998px;height:438px;background:var(--black);overflow:hidden}
.about-label{left:122px;top:62px;font-size:16px;color:var(--sky)}
.about-heading{left:122px;top:96px;width:380px;font-size:17.5px;line-height:22px;font-weight:700;color:var(--white);letter-spacing:.2px}
.about-copy{left:122px;top:152px;width:370px;font-size:11.3px;line-height:18.7px;color:#c8ccd6;letter-spacing:.2px}
.about-photo{left:574px;top:72px;width:278px;height:278px;border-radius:50%;background:linear-gradient(160deg,#eeeeec 0%,#c9ccd2 45%,#525c70 80%,#2c3342 100%)}

/* services */
.services{left:0;top:1004px;width:998px;height:393px}
.section-title{width:100%;text-align:center;font-size:16px;color:var(--blue)}
.section-sub{width:100%;text-align:center;font-size:11px;color:var(--ink)}
.offer{width:220px;text-align:center}
.offer-icon{width:34px;height:34px;margin:0 auto;background:var(--blue);border-radius:2px}
.offer h3{margin-top:10px;font-size:13.5px;font-weight:700;color:var(--ink)}
.offer em{display:block;font-style:normal;font-size:9.5px;font-weight:700;color:var(--blue);margin-top:1px}
.offer p{margin-top:11px;font-size:10.5px;line-height:18px;color:var(--soft);letter-spacing:.3px}

/* newsletter */
.newsletter{left:0;top:1397px;width:998px;height:128px;background:var(--black)}
.nl-kicker{left:56px;top:30px;font-size:8.5px;color:var(--sky)}
.nl-heading{left:56px;top:42px;font-size:16.5px;font-weight:700;color:var(--white)}
.nl-copy{left:56px;top:70px;font-size:10.5px;line-height:15px;color:#dfe2e8}
.nl-field{left:595px;top:48px;width:348px;height:32px;border:1px solid #c8ccd6;border-radius:16px;font-size:10px;color:var(--white);padding-left:17px;display:flex;align-items:center}
.nl-submit{left:786px;top:48px;width:157px;height:32px;border-radius:16px;background:var(--white);color:var(--ink);font-size:12.5px;font-weight:700;display:flex;align-items:center;justify-content:center}

/* engagements */
.engage{left:0;top:1525px;width:998px;height:403px;background:linear-gradient(180deg,#0c1f4a 0%,#08173a 55%,#02060e 100%)}
.engage-kicker{top:50px;font-family:'Roboto',sans-serif;font-size:16px;color:#b8bfcc}
.engage-title{top:75px;font-family:'Roboto',sans-serif;font-size:22px;color:var(--white)}
.post{top:1680px;width:210px;height:338px;background:var(--white);box-shadow:0 4px 14px rgba(0,0,0,.12)}
.post-media{position:absolute;left:17px;top:17px;width:176px;height:207px}
.post h4{position:absolute;left:17px;top:251px;width:180px;font-size:13px;line-height:18px;font-weight:700;color:var(--ink)}
.post p{position:absolute;left:17px;width:180px;font-size:10.5px;line-height:18px;color:var(--muted);letter-spacing:.2px}

/* footer */
.social{top:2146px;display:flex;align-items:center;gap:9px;font-size:12px;color:var(--ink)}
.social i{display:block;width:15px;height:15px;background:var(--ink)}
.copyright{right:62px;top:2147px;font-size:10.5px;color:var(--muted)}
</style>
</head>
<body>
  <div class="backdrop-shape" style="left:-420px;top:-200px;width:620px;height:520px"></div>
  <div class="backdrop-shape" style="left:860px;top:400px;width:760px;height:760px"></div>
  <div class="backdrop-shape" style="left:-300px;top:1700px;width:520px;height:600px"></div>
  <div class="backdrop-shape" style="left:700px;top:2250px;width:700px;height:500px"></div>

  <main class="page">
    <!-- hero -->
    <div class="abs hero-media" role="img" aria-label="Video still of the speaker on stage presenting in front of a projected screen"></div>
    <div class="abs play">
      <svg width="64" height="64" viewBox="0 0 64 64"><path d="M28 22 L42 32 L28 42 Z" fill="#111"/></svg>
    </div>

    <span class="abs nav" style="left:583px">Home</span>
    <span class="abs nav" style="left:643px">About Me</span>
    <span class="abs nav" style="left:723px">Services</span>
    <span class="abs nav" style="left:794px">Speaking</span>
    <span class="abs nav-cta">Contact Us</span>

    <p class="abs hero-name">Kostas Vranelis</p>
    <h1 class="abs hero-title">Digital Marketing<br>&amp; E-commerce<br>Expert</h1>
    <p class="abs hero-lead">No matter which service you choose, you can expect expert guidance, proven strategies, and measurable results.</p>
    <span class="btn btn-navy" style="left:536px;top:381px;width:134px;height:36px">Schedule a Call</span>
    <span class="btn btn-outline-navy" style="left:686px;top:381px;width:185px;height:36px">Download the Lead Magnet</span>

    <div class="abs stat" style="left:536px"><b>1,500+</b><span>students trained</span></div>
    <div class="abs stat" style="left:649px"><b>20+</b><span>Speeches</span></div>
    <div class="abs stat" style="left:734px"><b>122+</b><span>Online Courses</span></div>
    <div class="abs stat" style="left:844px"><b>100 %</b><span>Satisfaction</span></div>

    <!-- about -->
    <section class="abs about">
      <svg class="abs" style="left:0;top:0" width="998" height="438">
        <circle cx="755" cy="120" r="225" fill="none" stroke="#06204f" stroke-width="130"/>
        <circle cx="1020" cy="210" r="300" fill="#06204f"/>
      </svg>
      <p class="abs about-label">About me</p>
      <h2 class="abs about-heading">From Zero to 8 Figures: Our Story and Expertise in Business Growth</h2>
      <p class="abs about-copy">At our core, we're entrepreneurs just like you. We understand the struggles and challenges of growing a business from scratch. That's why we're passionate about sharing our decade of expertise in digital marketing and e-commerce with others. Over the years, we've worked with dozens of clients and helped them achieve explosive growth, scaling their businesses to multiple 6, 7, and even 8 figures. We believe that with the right strategies and guidance, any business can achieve great success. Let us share our story and expertise with you, and help you take your business to new heights."</p>
      <span class="btn btn-navy" style="left:122px;top:344px;width:114px;height:36px">Contact Us</span>
      <div class="abs about-photo" role="img" aria-label="Photo of two people seated in armchairs recording an interview in a studio"></div>
    </section>

    <!-- services -->
    <section class="abs services">
      <svg class="abs" style="left:0;top:0" width="998" height="393">
        <rect width="998" height="393" fill="#03070f"/>
        <path d="M0 0 H998 C930 110 930 290 998 393 H0 C68 290 68 110 0 0 Z" fill="#ffffff"/>
      </svg>
      <h2 class="abs section-title" style="top:36px">Our Services</h2>
      <p class="abs section-sub" style="top:61px">We offer solutions to help businesses succeed in today's digital landscape, including:</p>

      <div class="abs offer" style="left:125px;top:117px">
        <div class="offer-icon"><svg width="34" height="34"><rect x="10" y="15" width="3" height="9" fill="#fff"/><rect x="15.5" y="10" width="3" height="14" fill="#fff"/><rect x="21" y="18" width="3" height="6" fill="#fff"/></svg></div>
        <h3>Paid Ads</h3><em>Done for You</em>
        <p>Effective campaigns on Facenote, Snapgram, and Searchly that generate leads and sales fast.</p>
      </div>
      <div class="abs offer" style="left:388px;top:117px">
        <div class="offer-icon"><svg width="34" height="34"><rect x="10" y="15" width="3" height="9" fill="#fff"/><rect x="15.5" y="10" width="3" height="14" fill="#fff"/><rect x="21" y="18" width="3" height="6" fill="#fff"/></svg></div>
        <h3>Consulting/Mastermind</h3><em>Done with You</em>
        <p>Customized growth strategy with ongoing guidance and support, plus access to our exclusive Mastermind community.</p>
      </div>
      <div class="abs offer" style="left:652px;top:117px">
        <div class="offer-icon"><svg width="34" height="34"><rect x="10" y="15" width="3" height="9" fill="#fff"/><rect x="15.5" y="10" width="3" height="14" fill="#fff"/><rect x="21" y="18" width="3" height="6" fill="#fff"/></svg></div>
        <h3>Training</h3><em>Do it Yourself</em>
        <p>Learn digital marketing and e-commerce at your own pace with our comprehensive courses and resources.</p>
      </div>

      <span class="btn btn-blue" style="left:330px;top:327px;width:134px;height:36px">Schedule a Call</span>
      <span class="btn btn-outline-blue" style="left:481px;top:327px;width:185px;height:36px">Download the Lead Magnet</span>
    </section>

    <!-- newsletter -->
    <section class="abs newsletter">
      <p class="abs nl-kicker">Stay up-to-date with</p>
      <h2 class="abs nl-heading">the latest digital marketing and e-commerce strategies</h2>
      <p class="abs nl-copy">Get exclusive access to valuable content, expert advice,<br>and special offers delivered straight to your inbox.</p>
      <div class="abs nl-field">Enter Your email</div>
      <span class="abs nl-submit">Get Exclusive Content</span>
    </section>

    <!-- engagements -->
    <section class="abs engage">
      <p class="abs section-title engage-kicker">Latest Engagements</p>
      <h2 class="abs section-title engage-title">Our Latest Buzzworthy Moments and Accomplishments</h2>
    </section>

    <article class="abs post" style="left:52px">
      <div class="post-media" role="img" aria-label="Stage photo of a panel Q and A with two speakers" style="background:linear-gradient(180deg,#1e2430 0%,#8a7a3a 50%,#b8a450 100%)"></div>
      <h4>Boosting E-Commerce Sales</h4>
      <p style="top:290px">Looking to take your e-commerce store to the next level?</p>
    </article>
    <article class="abs post" style="left:280px">
      <div class="post-media" role="img" aria-label="Speaker on stage in front of a green event banner" style="background:linear-gradient(135deg,#1f8a5a 0%,#d8e8de 45%,#3a3a3a 100%)"></div>
      <h4>The Power of Paid Ads</h4>
      <p style="top:272px">Are you using paid ads to drive traffic to your website? In our latest blog post,</p>
    </article>
    <article class="abs post" style="left:507px">
      <div class="post-media" role="img" aria-label="Speaker presenting with a microphone in a bright room" style="background:linear-gradient(180deg,#cfcfcc 0%,#8a8680 55%,#2a2826 100%)"></div>
      <h4>the Art of Customer Retention</h4>
      <p style="top:290px">Looking to take your e-commerce store to the next level?</p>
    </article>
    <article class="abs post" style="left:734px">
      <div class="post-media" role="img" aria-label="Speaker with arms spread on a blue-lit conference stage" style="background:linear-gradient(180deg,#1fa0e0 0%,#1578c0 60%,#0c3a6a 100%)"></div>
      <h4>8-Figure Entrepreneurs</h4>
      <p style="top:272px">we'll share insights and lessons learned from successful entrepreneurs</p>
    </article>

    <span class="btn btn-blue" style="left:330px;top:2068px;width:134px;height:36px">Schedule a Call</span>
    <span class="btn btn-outline-blue" style="left:481px;top:2068px;width:185px;height:36px">Download the Lead Magnet</span>

    <!-- footer -->
    <div class="abs social" style="left:56px"><i></i>Proflink</div>
    <div class="abs social" style="left:158px"><i></i>Facenote</div>
    <div class="abs social" style="left:268px"><i></i>Chirper</div>
    <p class="abs copyright">Copyright © 2023 Kostas Vranelis. All rights reserved.</p>
  </main>
</body>
</html>
```